Business Card Design

Plumbing business.
Looking for a simple but professional looking design.
There are two variations of the logo; white background and black background. The logo with the white background is the primary business logo.
Industry/Entity Type
Business
Contact Information for Business Card
Marcus Fenley
Owner/Licensed Plumber
0412 396 081
info@marcusfenleyplumbing.com.au
www.marcusfenleyplumbing.com.au
Lic. 63941
Look and feel
Each slider illustrates characteristics of the customer's brand and the style your logo design should communicate.

```html
<!DOCTYPE html>
<html lang="en">
<head>
<meta charset="utf-8">
<title>Marcus Fenley Plumbing – Business Card</title>
<link href="https://fonts.googleapis.com/css2?family=Montserrat:wght@400;500;600&display=swap" rel="stylesheet">
<style>
  :root {
    --bg: #e4e4e2;
    --card-black: #0b0b0c;
    --card-black-soft: #2a2a2c;
    --strip-white: #f1f1f1;
    --teal: #2fb3c0;
    --white: #ffffff;
    --grey-text: #bdbdbd;
    --dark-text: #2b2b2b;
  }
  * { margin: 0; padding: 0; box-sizing: border-box; }
  html, body { width: 1200px; height: 1000px; overflow: hidden; }
  body {
    background: var(--bg);
    font-family: "Montserrat", sans-serif;
    position: relative;
  }
  .card {
    position: absolute;
    left: 250px;
    width: 700px;
    height: 400px;
    box-shadow: 0 10px 30px rgba(0,0,0,0.18);
    overflow: hidden;
  }
  /* Shared stacked wordmark */
  .wordmark { display: flex; align-items: center; white-space: nowrap; }
  .wordmark .mark-square { flex: none; background: var(--teal); }
  .wordmark .mark-text { display: flex; flex-direction: column; }
  .wordmark .mark-name {
    font-weight: 600;
    text-transform: uppercase;
    line-height: 1.05;
  }
  .wordmark .mark-trade {
    font-weight: 600;
    text-transform: uppercase;
  }

  /* Contact side */
  .card--contact { top: 70px; background: var(--card-black); display: flex; }
  .contact-strip {
    flex: none;
    width: 170px;
    height: 100%;
    background: var(--strip-white);
    position: relative;
  }
  .strip-wordmark {
    position: absolute;
    left: 50%;
    top: 50%;
    transform: translate(-50%, -50%) rotate(-90deg);
    gap: 14px;
  }
  .strip-wordmark .mark-square { width: 36px; height: 36px; }
  .strip-wordmark .mark-text {
    border-left: 1px solid #9a9a9a;
    padding-left: 14px;
  }
  .strip-wordmark .mark-name {
    font-size: 22px;
    letter-spacing: 1px;
    color: var(--dark-text);
  }
  .strip-wordmark .mark-trade {
    margin-top: 6px;
    font-size: 12px;
    letter-spacing: 9px;
    color: var(--dark-text);
  }
  .contact-body { padding: 80px 0 0 56px; color: var(--white); }
  .contact-name {
    font-weight: 500;
    font-size: 24px;
    letter-spacing: 3px;
  }
  .contact-role {
    margin-top: 6px;
    font-size: 11px;
    letter-spacing: 2px;
    text-transform: uppercase;
    color: var(--grey-text);
  }
  .contact-list { list-style: none; margin-top: 46px; }
  .contact-list li {
    display: flex;
    align-items: center;
    gap: 18px;
    font-size: 14px;
    letter-spacing: 1px;
    color: var(--grey-text);
    margin-bottom: 20px;
  }
  .contact-key {
    width: 18px; height: 18px;
    background: var(--teal);
    color: var(--card-black);
    font-size: 10px;
    font-weight: 600;
    display: flex; align-items: center; justify-content: center;
  }
  .contact-licence {
    margin-top: 18px;
    font-size: 11px;
    letter-spacing: 2px;
    color: var(--grey-text);
  }

  /* Brand side */
  .card--brand {
    top: 530px;
    background: radial-gradient(ellipse at 55% 45%, var(--card-black-soft) 0%, var(--card-black) 65%);
    display: flex;
    flex-direction: column;
    align-items: center;
    justify-content: center;
  }
  .brand-wordmark { gap: 20px; }
  .brand-wordmark .mark-square { width: 64px; height: 64px; }
  .brand-wordmark .mark-text {
    border-left: 1px solid #8a8a8a;
    padding-left: 20px;
  }
  .brand-wordmark .mark-name {
    font-size: 32px;
    letter-spacing: 2px;
    color: var(--white);
  }
  .brand-wordmark .mark-trade {
    margin-top: 8px;
    font-size: 15px;
    letter-spacing: 14px;
    color: var(--white);
  }
  .brand-web {
    margin-top: 18px;
    font-size: 12px;
    letter-spacing: 3px;
    text-transform: uppercase;
    color: var(--white);
  }
</style>
</head>
<body>
  <section class="card card--contact">
    <div class="contact-strip">
      <div class="wordmark strip-wordmark">
        <span class="mark-square"></span>
        <span class="mark-text">
          <span class="mark-name">Marcus</span>
          <span class="mark-name">Fenley</span>
          <span class="mark-trade">Plumbing</span>
        </span>
      </div>
    </div>
    <div class="contact-body">
      <h1 class="contact-name">Marcus Fenley</h1>
      <p class="contact-role">Owner/Licensed Plumber</p>
      <ul class="contact-list">
        <li><span class="contact-key">P</span>0412 396 081</li>
        <li><span class="contact-key">E</span>info@marcusfenleyplumbing.com.au</li>
        <li><span class="contact-key">W</span>www.marcusfenleyplumbing.com.au</li>
      </ul>
      <p class="contact-licence">Lic. 63941</p>
    </div>
  </section>

  <section class="card card--brand">
    <div class="wordmark brand-wordmark">
      <span class="mark-square"></span>
      <span class="mark-text">
        <span class="mark-name">Marcus</span>
        <span class="mark-name">Fenley</span>
        <span class="mark-trade">Plumbing</span>
      </span>
    </div>
    <p class="brand-web">www.marcusfenleyplumbing.com.au</p>
  </section>
</body>
</html>
```